Design for a Note buying company that attracts landlords and seller financed notes

I need a card designed. I want a simple clean front with my logo and contact info. On the back I want some big and bold words to get a message across.

Our Company buys Notes (mortgages) and we want to convey the sense of financial security. Our number one market that we pursue is tired landlords.

If you want to understand our business you can visit our website. www.lakeviewpaperfund.com

Do not use any Clip Art in the design, it will not be accepted. I want a custom designed card not something I could throw together myself. Simple clean and drive the message home.

Target Market(s)

Landlords, seller financed note holders

Industry/Entity Type

Mortgage

Contact Information for Business Card

Simple clean and bold. I need to grab the attention of the customer. It should convey a professional touch.

Font styles to use
Sans Serif

Colors
ec2229
ffffff

Requirements
Must have
• Clean front with logo and contact information
Front colors should match logo

Back should be bold and grab attention. Back colors are open to ideas
Nice to have
• The Back May use the phrase "No more Tentants, No more Toilets" "More Time, More Cash"

I'm open to other ideas about grabbing a landlords attention

I'm open to a square card design
I like cards with round corners as well
Should not have
• any clip art! must be custom designs.

```html
<!DOCTYPE html>
<html lang="en">
<head>
<meta charset="utf-8">
<title>Lakeview Paper Fund – Business Card</title>
<link rel="stylesheet" href="https://fonts.googleapis.com/css2?family=Arimo:wght@400;700&family=Exo+2:wght@600;700;800&display=swap">
<style>
  :root {
    --backdrop: #b5b5b5;
    --brand-red: #fe0000;
    --slogan-red: #ec2229;
    --ink-black: #000000;
    --paper-white: #ffffff;
    --rule-white: rgba(255,255,255,0.75);
  }
  * { margin: 0; padding: 0; box-sizing: border-box; }
  html, body { width: 1200px; height: 900px; overflow: hidden; }
  body { background: var(--backdrop); position: relative; }

  .card {
    position: absolute;
    top: 257px;
    width: 396px;
    height: 397px;
    border-radius: 28px;
    box-shadow: 3px 4px 6px rgba(0,0,0,0.45);
    color: var(--paper-white);
    text-align: center;
  }
  .card-front { left: 194px; background: var(--brand-red); font-family: "Arimo", Arial, sans-serif; }
  .card-back { left: 620px; width: 398px; background: var(--ink-black); font-family: "Exo 2", sans-serif; }

  .line { position: absolute; left: 0; right: 0; white-space: nowrap; }

  .holder-name { top: 97px; font-size: 22px; font-weight: 700; }
  .holder-title { top: 124px; font-size: 17px; }

  .icon-row { position: absolute; top: 161px; left: 0; right: 0; height: 26px; }
  .icon-rule { position: absolute; top: 13px; height: 1px; background: var(--rule-white); }
  .icon-rule.left { left: 95px; width: 54px; }
  .icon-rule.right { left: 250px; width: 52px; }
  .icon-box { position: absolute; top: 0; width: 26px; height: 26px; }
  .icon-phone { left: 155px; }
  .icon-mail { left: 187px; }
  .icon-web { left: 219px; }

  .contact { font-size: 17px; }
  .contact-phone { top: 199px; }
  .contact-email { top: 223px; }
  .contact-web { top: 246px; }
  .section-rule { position: absolute; top: 281px; left: 96px; width: 212px; height: 1px; background: var(--rule-white); }
  .address-1 { top: 291px; }
  .address-2 { top: 314px; }

  .tagline { top: 67px; font-size: 11px; font-weight: 700; letter-spacing: 4px; }
  .company-name { top: 99px; font-size: 34px; font-weight: 800; line-height: 44px; letter-spacing: 2px; }
  .slogan { font-size: 26px; font-weight: 700; color: var(--slogan-red); }
  .slogan-tenants { top: 236px; }
  .slogan-toilets { top: 271px; }
  .slogan-cash { top: 324px; }
</style>
</head>
<body>
  <section class="card card-front" aria-label="Card front">
    <div class="line holder-name">DANIEL REYES</div>
    <div class="line holder-title">Managing Director</div>

    <div class="icon-row">
      <span class="icon-rule left"></span>
      <svg class="icon-box icon-phone" viewBox="0 0 26 26" aria-label="Phone">
        <rect x="1" y="1" width="24" height="24" rx="3" fill="none" stroke="#fff" stroke-width="2"/>
        <path d="M8 7 l3 0 l1 3 l-2 1.5 a8 8 0 0 0 4 4 l1.5 -2 l3 1 l0 3 a2 2 0 0 1 -2 1.5 a11 11 0 0 1 -10 -10 a2 2 0 0 1 1.5 -2z" fill="none" stroke="#fff" stroke-width="1.5"/>
      </svg>
      <svg class="icon-box icon-mail" viewBox="0 0 26 26" aria-label="Email">
        <rect x="1" y="1" width="24" height="24" rx="3" fill="none" stroke="#fff" stroke-width="2"/>
        <rect x="6" y="8" width="14" height="10" fill="#fff"/>
        <path d="M6 8 l7 6 l7 -6" fill="none" stroke="#fe0000" stroke-width="1.4"/>
      </svg>
      <svg class="icon-box icon-web" viewBox="0 0 26 26" aria-label="Website">
        <rect x="1" y="1" width="24" height="24" rx="3" fill="none" stroke="#fff" stroke-width="2"/>
        <circle cx="13" cy="13" r="7" fill="#fff"/>
        <path d="M9 10 q3 -1 4 1 q-1 3 -3 3z M14 15 q3 -1 4 1 q-2 2 -4 2z" fill="#fe0000"/>
      </svg>
      <span class="icon-rule right"></span>
    </div>

    <div class="line contact contact-phone">044-555 210 384</div>
    <div class="line contact contact-email">info@lakeviewpaperfund.com</div>
    <div class="line contact contact-web">www.lakeviewpaperfund.com</div>
    <span class="section-rule"></span>
    <div class="line contact address-1">421, Address line goes here</div>
    <div class="line contact address-2">45452,Country Name</div>
  </section>

  <section class="card card-back" aria-label="Card back">
    <div class="line tagline">WE HELP PEOPLE LIVE!</div>
    <div class="line company-name">LAKEVIEW<br>PAPER FUND</div>
    <div class="line slogan slogan-tenants">No more Tentants</div>
    <div class="line slogan slogan-toilets">No more Toilets</div>
    <div class="line slogan slogan-cash">More Time, More Cash</div>
  </section>
</body>
</html>
```